SEO Company Needs a Professional, Bold Business Card Design

Kelvo SEO
2487 N Harlow Ave #315
Austin, TX 78751
512-555-0184
http://www.kelvoseo-demo.com
Kelvo SEO is an internet marketing company specializing in SEO for higher-end businesses. We are looking for a professional and bold (edgy) design that communicates our forward thinking SEO strategies. Our typical client is a small to medium US business that has never had SEO work done on their website but does has active marketing. We want our business card design to instill confidence in our services through a professional and bold look. We we would also like the design elements to be in line with the services we offer - ranking client websites in the search engine results, namely Zarnix.
Design Specifics:
Card design should have square edges.
Design should be delivered in fully layered and editable PSD file. Designing in AI is fine but I need a PSD file in case we have any changes in contact information or need additional cards for employees.
The design should compliment the attached logo.
Company Name:
Kelvo SEO
Address:
2487 N Harlow Ave #315
Austin, TX 78751
Personal Info:
Dorian Welk
Owner
theboss@kelvoseo-demo.com
Phone:
877-555-0139 (KELVO UP)
Website:
http://www.kelvoseo-demo.com
Slogan:
Could Your Website Be Generating More Business?
Target Market(s)
High-end business owners - doctors, lawyers, specialists, business owners doing 250k in profit.
Industry/Entity Type
Internet
Contact Information for Business Card
Company Name:
Kelvo SEO
Address:
2487 N Harlow Ave #315
Austin, TX 78751
Personal Info:
Dorian Welk
Owner
theboss@kelvoseo-demo.com
Phone:
877-555-0139 (KELVO UP)
Website:
www.kelvoseo-demo.com
Slogan:
Requirements
Must have
- Card design should have square edges.
- Background should be WHITE only.
- Design should be delivered in fully layered and editable PSD file. Designing in AI is fine but I need a PSD file in case we have any changes in contact information or need additional cards for employees.

```html
<!DOCTYPE html>
<html lang="en">
<head>
<meta charset="utf-8">
<title>Kelvo SEO Business Card</title>
<link href="https://fonts.googleapis.com/css2?family=Lato:wght@400;700&display=swap" rel="stylesheet">
<style>
  :root {
    --stage: #3b3b3b;
    --card-light: #ffffff;
    --card-edge: #e4e4e4;
    --brand-navy: #1f4784;
    --brand-cyan: #2bb3e3;
    --accent-red: #e2231a;
    --ink: #555555;
    --tagline: #1c2f6b;
  }
  * { margin: 0; padding: 0; box-sizing: border-box; }
  html, body {
    width: 1200px; height: 750px; overflow: hidden;
    background: var(--stage);
    font-family: "Lato", sans-serif;
  }
  .canvas { position: relative; width: 1200px; height: 750px; }
  .card {
    position: absolute; top: 218px; width: 504px; height: 287px;
    background: radial-gradient(ellipse at 50% 30%, var(--card-light) 35%, var(--card-edge) 100%);
  }
  .card--front { left: 81px; }
  .card--back { left: 617px; }

  .brand { display: flex; align-items: center; gap: 8px; color: var(--brand-navy); font-weight: 700; white-space: nowrap; }
  .brand__dot { border-radius: 50%; background: var(--brand-navy); flex: none; }

  .card--front .brand { position: absolute; left: 40px; top: 128px; font-size: 32px; }
  .card--front .brand__dot { width: 22px; height: 22px; }

  .contact { position: absolute; left: 309px; top: 72px; color: var(--ink); font-size: 12px; line-height: 1; }
  .contact__name { color: var(--brand-cyan); font-weight: 700; font-size: 16px; }
  .contact__role { color: var(--brand-navy); font-size: 12px; margin-top: 4px; }
  .contact__list { list-style: none; margin-top: 19px; }
  .contact__list li { display: flex; align-items: center; gap: 8px; height: 14.5px; }
  .contact__list svg { width: 11px; height: 11px; flex: none; }
  .contact__web-name { color: var(--accent-red); }
  .contact__address { margin-top: 16px; line-height: 15px; font-style: normal; }

  .card--back .brand { position: absolute; left: 0; right: 0; top: 126px; justify-content: center; font-size: 46px; }
  .card--back .brand__dot { width: 30px; height: 30px; }
  .tagline {
    position: absolute; left: 0; right: 0; top: 186px; text-align: center;
    color: var(--tagline); font-size: 12.5px; font-weight: 700;
  }
</style>
</head>
<body>
<main class="canvas">
  <section class="card card--front">
    <div class="brand"><span class="brand__dot"></span>Kelvo SEO</div>
    <div class="contact">
      <div class="contact__name">Dorian Welk</div>
      <div class="contact__role">Owner</div>
      <ul class="contact__list">
        <li>
          <svg viewBox="0 0 12 12"><path fill="#2bb3e3" d="M2.4 1 4 .6l1.3 2.6-1 .9a6 6 0 0 0 3.6 3.6l.9-1 2.6 1.3-.4 1.6C10.6 10.8 9 11.5 7 10.6 4.5 9.5 2.5 7.5 1.4 5 .6 3 1.2 1.4 2.4 1Z"/></svg>
          877-555-0139
        </li>
        <li>
          <svg viewBox="0 0 12 12"><rect x="0.5" y="2" width="11" height="8" fill="#2bb3e3"/><path d="M0.8 2.4 6 6.6l5.2-4.2" fill="none" stroke="#fff" stroke-width="1"/></svg>
          theboss@kelvoseo-demo.com
        </li>
        <li>
          <svg viewBox="0 0 12 12" fill="none" stroke="#2bb3e3" stroke-width="0.9"><circle cx="6" cy="6" r="5.2"/><ellipse cx="6" cy="6" rx="2.3" ry="5.2"/><path d="M.8 6h10.4M1.8 3.3h8.4M1.8 8.7h8.4"/></svg>
          <span>www.<span class="contact__web-name">kelvoseo-demo</span>.com</span>
        </li>
      </ul>
      <address class="contact__address">2487 N Harlow Ave #315<br>Austin, TX 78751</address>
    </div>
  </section>

  <section class="card card--back">
    <div class="brand"><span class="brand__dot"></span>Kelvo SEO</div>
    <p class="tagline">Could Your Website Be Generating More Business?</p>
  </section>
</main>
</body>
</html>
```